Business card for massage therapy company called Brook Fern Wellness

Need business card for massage therapy company called Brook Fern Wellness. Would like my logo on the front and the back of the card I have 3 options of logos and you can play with what looks better.

Would like this information displayed on the back of the card:

Marcus Ellery
Licensed Massage Therapist
321-555-0147
brookfern-example.com
brookfern_rest_

```html
<!DOCTYPE html>
<html lang="en">
<head>
<meta charset="utf-8">
<title>Brook Fern Wellness – Business Card</title>
<link href="https://fonts.googleapis.com/css2?family=Questrial&family=Open+Sans:wght@400&display=swap" rel="stylesheet">
<style>
  :root{
    --backdrop:#1c1c1c;
    --sage:#747b63;
    --sage-light:#8a9079;
    --sage-text:#6f7561;
    --cream:#fbf8ee;
    --cream-warm:#f6efdc;
    --ink:#5f6552;
    --petal:#efe0a8;
    --leaf:#7f9a78;
    --white:#ffffff;
  }
  *{box-sizing:border-box;margin:0;padding:0}
  html,body{width:1200px;height:886px;overflow:hidden;background:var(--backdrop)}
  .canvas{position:relative;width:1200px;height:886px}
  .card{position:absolute;width:560px;height:320px;border-radius:22px;overflow:hidden}

  /* Logo side */
  .card--logo{left:320px;top:90px;background:linear-gradient(120deg,var(--sage) 0%,var(--sage-light) 60%,var(--sage) 100%)}
  .card__pattern{position:absolute;inset:0;background:linear-gradient(120deg,rgba(255,255,255,.03),rgba(255,255,255,.08),rgba(255,255,255,.03))}
  .brand-mark{position:absolute;left:50%;top:50%;transform:translate(-50%,-50%);display:flex;align-items:center;gap:14px}
  .brand-mark__circle{width:64px;height:64px;border:2px solid var(--white);border-radius:50%}
  .brand-mark__name{font-family:'Questrial',sans-serif;font-size:30px;color:var(--white);letter-spacing:1px}

  /* Contact side */
  .card--contact{left:320px;top:476px;background:linear-gradient(135deg,var(--white) 0%,var(--cream) 45%,var(--cream-warm) 100%)}
  .wash{position:absolute;border-radius:50%;filter:blur(6px)}
  .wash--corner{right:-30px;top:-30px;width:110px;height:110px;background:radial-gradient(circle,var(--petal),transparent 70%)}
  .wash--leaves{right:-20px;top:110px;width:80px;height:120px;background:radial-gradient(ellipse,var(--leaf),transparent 70%);opacity:.8}
  .wash--rose{left:-30px;bottom:-30px;width:150px;height:140px;background:radial-gradient(circle,var(--petal),transparent 70%)}

  .wordmark{position:absolute;left:56px;top:70px;font-family:'Questrial',sans-serif;font-size:40px;color:var(--sage-text);letter-spacing:1px}
  .person{position:absolute;right:48px;top:150px;text-align:left}
  .person__name{font-family:'Questrial',sans-serif;font-size:30px;color:var(--ink)}
  .person__title{font-family:'Open Sans',sans-serif;font-size:12px;letter-spacing:.6px;color:var(--ink);text-transform:uppercase;margin-top:2px}
  .contact{position:absolute;left:56px;bottom:40px;font-family:'Open Sans',sans-serif;font-size:16px;line-height:1.45;color:var(--ink);list-style:none}
</style>
</head>
<body>
<main class="canvas">
  <section class="card card--logo" aria-label="Card logo side">
    <div class="card__pattern" role="img" aria-label="Faint repeated brand name pattern"></div>
    <div class="brand-mark">
      <span class="brand-mark__circle"></span>
      <span class="brand-mark__name">Brook Fern Wellness</span>
    </div>
  </section>

  <section class="card card--contact" aria-label="Card contact side">
    <div class="wash wash--corner" role="img" aria-label="Watercolour yellow leaf"></div>
    <div class="wash wash--leaves" role="img" aria-label="Watercolour green leaves"></div>
    <div class="wash wash--rose" role="img" aria-label="Watercolour yellow rose"></div>

    <h1 class="wordmark">Brook Fern Wellness</h1>
    <div class="person">
      <p class="person__name">Marcus Ellery</p>
      <p class="person__title">Licensed Massage Therapist</p>
    </div>
    <ul class="contact">
      <li>321-555-0147</li>
      <li>brookfern-example.com</li>
      <li>@brookfern_rest_</li>
    </ul>
  </section>
</main>
</body>
</html>
```